Rooted Ready Rising: Quiet Roots, Open Doors, Steady Hands

I want a modern and clean looking book cover. 5.25x8

Title
Rooted Ready Rising

Subtitle
Quiet Roots, Open Doors, Steady Hands

I don’t just want a graphic, I want it to make sense. If it can just be the words and a textured looking background, I’ll be ok with that too. I just want it to look crisp, clean, modern.

I want the back to have my book blurb and bio attached with the pic that’s attached.

Target Market(s)

Self help

Requirements
Must have
• Modern, clean look, look professional, attract customers.

```html
<!DOCTYPE html>
<html lang="en">
<head>
<meta charset="utf-8">
<title>Rooted Ready Rising — Cover Spread</title>
<link href="https://fonts.googleapis.com/css2?family=Anton&family=Oswald:wght@600;700&family=Open+Sans:wght@400;700;800&display=swap" rel="stylesheet">
<style>
  :root {
    --backdrop: #ffffff;
    --title-red: #e8322b;
    --tagline-red: #e0302a;
    --ink-dark: #2b2b2b;
    --paper-white: #ffffff;
    --back-text: #e9e9e9;
    --sky-light: #d9d9d9;
    --sky-mid: #a9a9a9;
    --forest-mid: #5c5c5c;
    --forest-dark: #1f1f1f;
    --back-top: #6a6a6a;
    --back-bottom: #0d0d0d;
  }
  * { box-sizing: border-box; margin: 0; padding: 0; }
  html, body { width: 1200px; height: 1000px; overflow: hidden; background: var(--backdrop); }
  .spread {
    position: relative; width: 1200px; height: 1000px;
    display: flex; justify-content: center; align-items: center; gap: 44px;
  }
  .cover { position: relative; width: 538px; height: 820px; overflow: hidden; }

  /* Back cover */
  .back-photo {
    position: absolute; inset: 0;
    background: linear-gradient(180deg, var(--back-top) 0%, #3a3a3a 35%, #1c1c1c 70%, var(--back-bottom) 100%);
  }
  .back-content {
    position: absolute; inset: 0; padding: 44px 38px 36px;
    font-family: "Open Sans", sans-serif; color: var(--back-text);
    font-size: 12.4px; line-height: 1.42;
  }
  .bio p { margin-bottom: 3px; }
  .bio strong { color: var(--paper-white); font-weight: 800; }
  .tagline {
    margin: 24px 0 18px; text-align: center;
    font-weight: 800; font-size: 17px; line-height: 1.3; color: var(--tagline-red);
  }
  .blurb { text-align: center; }
  .blurb p { margin-bottom: 12px; }

  /* Front cover */
  .front-photo {
    position: absolute; inset: 0;
    background:
      radial-gradient(circle at 14% 33%, rgba(255,255,255,0.95) 0, rgba(255,255,255,0.5) 4%, rgba(255,255,255,0) 14%),
      linear-gradient(180deg, var(--sky-light) 0%, #bdbdbd 22%, var(--sky-mid) 40%, #8a8a8a 52%, var(--forest-mid) 68%, #3a3a3a 84%, var(--forest-dark) 100%);
  }
  .subtitle {
    position: absolute; top: 30px; left: 0; right: 0; text-align: center;
    font-family: "Oswald", sans-serif; font-weight: 700; font-size: 23px;
    color: var(--ink-dark); letter-spacing: 0.2px;
  }
  .title {
    position: absolute; left: 0; right: 0; top: 100px;
    font-family: "Anton", sans-serif; color: var(--title-red); opacity: 0.88;
    text-align: center; text-transform: uppercase; line-height: 1;
  }
  .title span { display: block; font-size: 124px; letter-spacing: 2px; }
  .title .line-one { margin-bottom: 120px; }
  .title .line-two { margin-bottom: 8px; }
  .author {
    position: absolute; bottom: 50px; left: 0; right: 0; text-align: center;
    font-family: "Open Sans", sans-serif; font-weight: 700; font-size: 30px;
    color: var(--paper-white);
  }
</style>
</head>
<body>
<main class="spread">
  <section class="cover cover-back">
    <div class="back-photo" role="img" aria-label="Dark misty forest hillside photograph in black and white"></div>
    <div class="back-content">
      <div class="bio">
        <p><strong>Lena Marsh</strong> is a helper.</p>
        <p>For as long as she can remember, she's always wanted to lift others up. But circumstance, and some very tough years, set her on a path that often conflicted with what was in her heart... until something shifted and she made herself and her goals a priority.</p>
        <p>A dreamer and visionary at her core, she knows all too well how much faith and courage it takes to defy expectations and carve your own path forward. Her tenacity led her in a direction that would change her life for the better.</p>
        <p>After being told she wasn't "college material" in high school, she made it her mission to never allow anyone to define who she is, and more importantly, to empower others to do the same.</p>
        <p>Today, the devout Christian, Author, Motivator, Coach and Educational Leader, holds 3 degrees (Bachelors in Psychology, Master of Education, and Educational Specialist) and is currently in the dissertation phase of a Doctorate of Education. Recently, she added Life Coach to her resume.</p>
        <p>When she's not teaching, studying, coaching, reading, listening to music, or helping others achieve their goals, she spends as much time as she can with her loving husband, their school-aged God-daughter, and countless friends.</p>
      </div>
      <p class="tagline">Everyone has big dreams,<br>but few give themselves permission.</p>
      <div class="blurb">
        <p>Rooted Ready Rising: Quiet Roots, Open Doors, Steady Hands is for anyone who has ever been stymied by negative self-talk, maltreatment, money problems, or has experienced anything significant that derailed their dreams.</p>
        <p>Part memoir, part self-help book, part spiritual guide, it offers encouragement and a helping hand to anyone who feels like their time has passed, or that their time will never come.</p>
        <p>Inside, you'll find deeply personal stories and anecdotes. These personal experiences provide a detailed account and a guide to climb out of a dark spot, find your voice, dream bigger, dare to believe again. If you've ever felt like where you are now is where you'll stay, or that your prayers will never be answered, this book will help you move forward and learn how to confidently bet on yourself.</p>
      </div>
    </div>
  </section>

  <section class="cover cover-front">
    <div class="front-photo" role="img" aria-label="Black and white photograph of misty forested hills under a bright sun breaking through clouds"></div>
    <p class="subtitle">Quiet Roots, Open Doors, Steady Hands</p>
    <h1 class="title">
      <span class="line-one">Rooted</span>
      <span class="line-two">Ready</span>
      <span class="line-three">Rising</span>
    </h1>
    <p class="author">Lena Marsh</p>
  </section>
</main>
</body>
</html>
```